Business card design needed for Automotive Reconditioning business

I have a logo design i just cant decide on the best color or layout for the business card, I will upload all the files so you can see all colors schemes we are considering. I have other file formats if needed let me know.

Target Market(s)

automotive dealerships

Contact Information for Business Card

HERE are the Descriptions and info needed on the card:
Interior Repair: Leather carpet burns panels dash Deoderize
Dealer products and Vin Verify
( spot for name and cell number) My name is Norman Bexley phone 614 352-4180 Title COO www.QuorvalMotive.com

Font styles to use
Sans Serif
Other font styles liked:
• what ever you think looks best

Requirements
Must have
• Must be able to change the name and phone for employees

```html
<!DOCTYPE html>
<html lang="en">
<head>
<meta charset="utf-8">
<title>Quorval Motive – Business Card</title>
<link rel="stylesheet" href="https://fonts.googleapis.com/css2?family=Quicksand:wght@400;500;700&display=swap">
<style>
  :root {
    --page-bg: #3a3d42;
    --card-bg: #232323;
    --card-edge: #1a1a1a;
    --brand-red: #e23a2c;
    --brand-blue: #2a8fd8;
    --text-light: #e9e9e9;
    --text-muted: #bdbdbd;
    --rule: #8c8c8c;
    --ghost: rgba(255, 255, 255, 0.035);
  }
  * { box-sizing: border-box; margin: 0; padding: 0; }
  html, body {
    width: 1200px;
    height: 900px;
    overflow: hidden;
    background: var(--page-bg);
    font-family: "Quicksand", sans-serif;
  }
  .canvas {
    width: 1200px;
    height: 900px;
    display: flex;
    align-items: center;
    justify-content: center;
  }
  .business-card {
    position: relative;
    width: 1000px;
    height: 572px;
    background: var(--card-bg);
    border-radius: 36px;
    box-shadow: 0 14px 40px rgba(0, 0, 0, 0.45);
    overflow: hidden;
    color: var(--text-light);
  }
  .card-backdrop {
    position: absolute;
    left: 90px;
    top: 170px;
    width: 820px;
    height: 340px;
    border-radius: 200px 260px 60px 60px;
    background: radial-gradient(ellipse at center, var(--ghost), transparent 70%);
  }
  .card-content {
    position: relative;
    height: 100%;
    display: flex;
    flex-direction: column;
    align-items: center;
    padding-top: 78px;
  }
  .brand {
    display: flex;
    align-items: center;
    gap: 18px;
  }
  .brand-dot {
    width: 22px;
    height: 22px;
    border-radius: 50%;
    background: var(--brand-red);
  }
  .brand-name {
    font-weight: 700;
    color: var(--brand-red);
    text-transform: uppercase;
    line-height: 1.05;
    text-align: center;
  }
  .brand-name .line-main { display: block; font-size: 54px; letter-spacing: 2px; }
  .brand-name .line-sub { display: block; font-size: 22px; letter-spacing: 3px; margin-top: 6px; }
  .person {
    margin-top: 46px;
    text-align: center;
  }
  .person-name {
    font-size: 42px;
    font-weight: 500;
  }
  .person-name .first { color: var(--brand-blue); }
  .person-name .last { color: var(--brand-red); }
  .person-title {
    font-size: 30px;
    font-weight: 400;
    color: var(--text-muted);
    letter-spacing: 3px;
    margin-top: 2px;
  }
  .contact-rule {
    display: flex;
    align-items: center;
    width: 420px;
    margin-top: 26px;
  }
  .contact-rule .rule {
    flex: 1;
    height: 1px;
    background: var(--rule);
  }
  .contact-icons {
    display: flex;
    gap: 8px;
    padding: 0 10px;
  }
  .contact-icon { width: 22px; height: 22px; }
  .contact-list {
    margin-top: 14px;
    text-align: center;
    font-size: 24px;
    font-weight: 500;
    line-height: 1.45;
    color: var(--text-light);
  }
</style>
</head>
<body>
<main class="canvas">
  <article class="business-card">
    <div class="card-backdrop" role="img" aria-label="Faint vehicle silhouette decoration"></div>
    <div class="card-content">
      <header class="brand">
        <span class="brand-dot"></span>
        <h1 class="brand-name">
          <span class="line-main">Quorval Motive</span>
          <span class="line-sub">Reconditioning Corp.</span>
        </h1>
      </header>

      <section class="person">
        <p class="person-name"><span class="first">Norman</span> <span class="last">Bexley</span></p>
        <p class="person-title">COO</p>
      </section>

      <div class="contact-rule">
        <span class="rule"></span>
        <span class="contact-icons">
          <svg class="contact-icon" viewBox="0 0 24 24" aria-hidden="true">
            <circle cx="12" cy="12" r="11" fill="#ffffff"/>
            <path d="M8.2 6.5l2 2.3-1.1 1.4c.8 1.7 2 2.9 3.7 3.7l1.4-1.1 2.3 2-1.2 1.8c-4.2-.5-7.9-4.2-8.4-8.4z" fill="#232323"/>
          </svg>
          <svg class="contact-icon" viewBox="0 0 24 24" aria-hidden="true">
            <circle cx="12" cy="12" r="11" fill="#ffffff"/>
            <g fill="none" stroke="#232323" stroke-width="1.3">
              <circle cx="12" cy="12" r="6"/>
              <ellipse cx="12" cy="12" rx="2.6" ry="6"/>
              <line x1="6" y1="12" x2="18" y2="12"/>
            </g>
          </svg>
        </span>
        <span class="rule"></span>
      </div>

      <address class="contact-list" style="font-style: normal;">
        <p class="contact-phone">614 352-4180</p>
        <p class="contact-web">www.QuorvalMotive.com</p>
      </address>
    </div>
  </article>
</main>
</body>
</html>
```